Business card for a shop called "Bright loom company"

the shop are selling disposable wooden packaging cutlery, wooden trays, wooden plates, carton, box, adhesive, stretch film...
Fully recyclable and 100% wood.
We want something futuristic and good for the planet

Target Market(s)

professional customers, company, fast-food, restaurant, caterer,

Industry/Entity Type

wood furnitures for food

Contact Information for Business Card

Colors

Designer to choose colors to be used in the design.

Requirements
Must have
• QR CODE, selective varnish on the given logo, brown and neon green light color. Name and surname, function (CEO), tel, mail and address.
Nice to have
• minimalist design , futuristic and ecology
Should not have
• the list of furniture we are selling.

```html
<!DOCTYPE html>
<html lang="en">
<head>
<meta charset="utf-8">
<title>Bright loom company – Business Card</title>
<link rel="stylesheet" href="https://fonts.googleapis.com/css2?family=Delius&family=Open+Sans:wght@400;600&display=swap">
<style>
  :root {
    --page-bg: #e9e6e1;
    --card-dark: #141414;
    --card-mid: #262626;
    --neon-green: #8ff59a;
    --wood-brown: #c8923f;
    --shadow: rgba(0, 0, 0, 0.28);
  }
  * { box-sizing: border-box; margin: 0; padding: 0; }
  html, body {
    width: 1200px;
    height: 900px;
    overflow: hidden;
    background: var(--page-bg);
  }
  .canvas {
    position: relative;
    width: 1200px;
    height: 900px;
  }
  .card {
    position: absolute;
    left: 260px;
    width: 680px;
    height: 388px;
    border-radius: 4px;
    overflow: hidden;
    box-shadow: 0 10px 28px var(--shadow);
  }
  .card--back { top: 40px; }
  .card--front { top: 472px; }
  .card__surface {
    position: absolute;
    inset: 0;
    background: linear-gradient(160deg, var(--card-mid) 0%, var(--card-dark) 55%, #0d0d0d 100%);
  }

  /* Back side */
  .holder {
    position: absolute;
    left: 130px;
    top: 196px;
    text-align: right;
  }
  .holder__name {
    font-family: "Delius", cursive;
    font-size: 40px;
    color: var(--neon-green);
    line-height: 1;
  }
  .holder__role {
    font-family: "Open Sans", sans-serif;
    font-size: 14px;
    color: var(--wood-brown);
    margin-top: 6px;
    letter-spacing: 0.5px;
  }
  .contacts {
    position: absolute;
    left: 400px;
    top: 78px;
    list-style: none;
    font-family: "Open Sans", sans-serif;
    font-size: 15px;
    color: var(--wood-brown);
  }
  .contacts li {
    display: flex;
    align-items: center;
    gap: 9px;
    margin-bottom: 7px;
  }
  .contacts svg { width: 14px; height: 14px; flex: none; }
  .address {
    position: absolute;
    left: 130px;
    bottom: 56px;
    display: flex;
    align-items: center;
    gap: 10px;
    font-family: "Open Sans", sans-serif;
    font-size: 15px;
    color: var(--wood-brown);
  }
  .address svg { width: 16px; height: 20px; }

  /* Front side */
  .brand {
    position: absolute;
    inset: 0;
    display: flex;
    align-items: center;
    justify-content: center;
    gap: 16px;
  }
  .brand__dot {
    width: 22px;
    height: 22px;
    border-radius: 50%;
    background: var(--wood-brown);
  }
  .brand__name {
    font-family: "Delius", cursive;
    font-size: 44px;
    color: var(--neon-green);
  }
</style>
</head>
<body>
<main class="canvas">

  <section class="card card--back" aria-label="Business card, contact side">
    <div class="card__surface" role="img" aria-label="Dark charcoal wood grain texture"></div>

    <div class="holder">
      <p class="holder__name">Owen Calder</p>
      <p class="holder__role">CEO</p>
    </div>

    <ul class="contacts">
      <li>
        <svg viewBox="0 0 16 16" aria-hidden="true"><path fill="#8ff59a" d="M4 1.5l2.2 3-1.3 1.6c.8 1.9 2.4 3.5 4.3 4.3l1.6-1.3 3 2.2-1.2 2.6C7.4 13.6 2.4 8.6 1.4 2.7z"/></svg>
        (555) 014-2290
      </li>
      <li>
        <svg viewBox="0 0 16 16" aria-hidden="true"><rect x="1" y="3" width="14" height="10" rx="1.5" fill="#8ff59a"/><path d="M1.5 4l6.5 5 6.5-5" fill="none" stroke="#141414" stroke-width="1.3"/></svg>
        hello@brightloomco.com
      </li>
      <li>
        <svg viewBox="0 0 16 16" aria-hidden="true"><circle cx="8" cy="8" r="7" fill="#8ff59a"/><path d="M5 8h6M8 5v6" stroke="#141414" stroke-width="1.4"/></svg>
        www.brightloomco.com
      </li>
    </ul>

    <p class="address">
      <svg viewBox="0 0 16 20" aria-hidden="true"><path fill="#8ff59a" d="M8 0a7 7 0 0 0-7 7c0 5 7 13 7 13s7-8 7-13a7 7 0 0 0-7-7z"/><circle cx="8" cy="7" r="2.6" fill="#141414"/></svg>
      412 Cedar Hollow Road Alder Springs, CA 95010
    </p>
  </section>

  <section class="card card--front" aria-label="Business card, brand side">
    <div class="card__surface" role="img" aria-label="Dark charcoal wood grain texture"></div>
    <div class="brand">
      <span class="brand__dot" aria-hidden="true"></span>
      <p class="brand__name">Bright loom company</p>
    </div>
  </section>

</main>
</body>
</html>
```